Corvane Electronics, Inc. Business card

Incorporate a globe.
We repair electronics, sell electronic parts, and we recycle electronics. We've been in business since 1982. A technology feel to the card is preferred. I want to be able to give this card to a client from different industries and make it relate-able. I don't have a logo that I've been partial to in the past. It is not necessary in this case.

Target Market(s)

Consumer, Industrial, Business, Medical

Industry/Entity Type

Business

Contact Information for Business Card

4518 Maple Crest Blvd. Dallas, TX 75207
214-555-0187 main 214-555-0143 fax
Paul Bredesen VP

Font styles to use
Serif

Requirements
Must have
• Technology feel
Nice to have
• Metallic look
Should not have
• no pastel colors

```html
<!DOCTYPE html>
<html lang="en">
<head>
<meta charset="utf-8">
<title>Corvane Electronics, Inc. – Business Card</title>
<link rel="stylesheet" href="https://fonts.googleapis.com/css2?family=Source+Serif+4:wght@400;600;700&display=swap">
<style>
  :root {
    --backdrop: #2b2b2d;
    --card-dark: #141416;
    --card-sheen: #2a2a2e;
    --panel: #1c1c1f;
    --accent-red: #c4262b;
    --accent-red-deep: #7a1216;
    --silver: #d9d9dc;
    --silver-dim: #8d8d93;
    --text-light: #ececec;
  }
  * { margin: 0; padding: 0; box-sizing: border-box; }
  html, body {
    width: 1200px;
    height: 900px;
    overflow: hidden;
    background: var(--backdrop);
    font-family: "Source Serif 4", Georgia, serif;
  }
  .stage {
    width: 1200px;
    height: 900px;
    display: flex;
    align-items: center;
    justify-content: center;
    gap: 50px;
  }
  .card {
    width: 520px;
    height: 300px;
    border-radius: 22px;
    background: linear-gradient(135deg, var(--card-sheen) 0%, var(--card-dark) 38%, var(--card-dark) 70%, #232327 100%);
    box-shadow: 0 14px 30px rgba(0,0,0,0.45), inset 0 1px 0 rgba(255,255,255,0.08);
    position: relative;
    overflow: hidden;
  }
  .globe {
    display: block;
    border-radius: 50%;
    background: radial-gradient(circle at 35% 30%, #e9e9ec 0%, var(--silver-dim) 30%, var(--accent-red) 62%, var(--accent-red-deep) 100%);
    box-shadow: 0 0 0 2px rgba(217,217,220,0.25);
    flex: none;
  }
  .tech-rule {
    position: absolute;
    left: 0;
    right: 0;
    height: 1px;
    background: linear-gradient(90deg, transparent, var(--silver-dim), transparent);
  }

  /* Contact side */
  .card-contact { display: flex; }
  .brand-side {
    width: 42%;
    display: flex;
    flex-direction: column;
    align-items: center;
    justify-content: center;
    gap: 16px;
  }
  .brand-side .globe { width: 120px; height: 120px; }
  .brand-name-small {
    color: var(--silver);
    font-size: 14px;
    font-weight: 600;
    letter-spacing: 0.3px;
    white-space: nowrap;
  }
  .details-side {
    width: 58%;
    background: var(--panel);
    border-left: 1px solid rgba(217,217,220,0.12);
    padding: 74px 20px 0 26px;
  }
  .person-name {
    color: var(--accent-red);
    font-size: 19px;
    font-weight: 700;
    margin-bottom: 14px;
  }
  .contact-line {
    display: flex;
    align-items: center;
    gap: 10px;
    color: var(--text-light);
    font-size: 13px;
    margin-bottom: 5px;
  }
  .contact-line svg { width: 11px; height: 11px; flex: none; }
  .address {
    color: var(--text-light);
    font-size: 12px;
    margin-top: 22px;
    white-space: nowrap;
  }

  /* Brand side */
  .card-brand {
    display: flex;
    flex-direction: column;
    align-items: center;
    justify-content: center;
    gap: 18px;
  }
  .card-brand .globe { width: 100px; height: 100px; }
  .brand-name-large {
    color: var(--accent-red);
    font-size: 30px;
    font-weight: 600;
    letter-spacing: 0.5px;
    white-space: nowrap;
  }
</style>
</head>
<body>
<main class="stage">
  <section class="card card-contact" aria-label="Business card, contact side">
    <div class="brand-side">
      <span class="globe" role="img" aria-label="Globe emblem"></span>
      <span class="brand-name-small">Corvane Electronics, Inc.</span>
    </div>
    <div class="details-side">
      <p class="person-name">Paul Bredesen VP</p>
      <p class="contact-line">
        <svg viewBox="0 0 24 24" aria-hidden="true"><path fill="var(--accent-red)" d="M6.6 10.8a15.1 15.1 0 0 0 6.6 6.6l2.2-2.2c.3-.3.7-.4 1-.2 1.1.4 2.3.6 3.6.6.6 0 1 .4 1 1V20c0 .6-.4 1-1 1A17 17 0 0 1 3 4c0-.6.4-1 1-1h3.5c.6 0 1 .4 1 1 0 1.3.2 2.5.6 3.6.1.3 0 .7-.2 1z"/></svg>
        214-555-0187
      </p>
      <p class="contact-line">
        <svg viewBox="0 0 24 24" aria-hidden="true"><path fill="var(--accent-red)" d="M9 3h6a1 1 0 0 1 1 1v2h4a2 2 0 0 1 2 2v10a2 2 0 0 1-2 2H4a2 2 0 0 1-2-2V8a2 2 0 0 1 2-2h4V4a1 1 0 0 1 1-1zm1 3h4V5h-4z"/></svg>
        214-555-0143
      </p>
      <p class="address">4518 Maple Crest Blvd. Dallas, TX 75207</p>
    </div>
    <span class="tech-rule" style="bottom: 26px;"></span>
  </section>

  <section class="card card-brand" aria-label="Business card, brand side">
    <span class="globe" role="img" aria-label="Globe emblem"></span>
    <span class="brand-name-large">Corvane Electronics, Inc.</span>
    <span class="tech-rule" style="bottom: 26px;"></span>
  </section>
</main>
</body>
</html>
```